Fernlake Business Card Design

We are looking for a fresh business card design for our new logo. We would like a business card that is unique but friendly. We are in the window coverings business offering blinds, shutters and shades for homes.

Target Market(s)

Targeting the end-consumer

Industry/Entity Type

Business

Requirements
Must have
• Must have a dedicates space for a photo of our sales person. Must contain our new logo (attached).

```html
<!DOCTYPE html>
<html lang="en">
<head>
<meta charset="utf-8">
<title>Fernlake Business Card</title>
<link rel="stylesheet" href="https://fonts.googleapis.com/css2?family=Source+Sans+3:wght@400;600&display=swap">
<style>
  :root {
    --backdrop: #000000;
    --card: #323335;
    --card-edge: #3a3b3e;
    --mark-grey: #76777a;
    --leaf-green: #8cc63f;
    --text-white: #f4f4f4;
    --divider: #2a2b2d;
    --photo-fill: #3d3e41;
  }
  * { margin: 0; padding: 0; box-sizing: border-box; }
  html, body {
    width: 1200px;
    height: 900px;
    overflow: hidden;
    background: var(--backdrop);
    font-family: "Source Sans 3", "Helvetica Neue", Arial, sans-serif;
  }
  .canvas { position: relative; width: 1200px; height: 900px; }
  .card {
    position: absolute;
    top: 271px;
    width: 457px;
    height: 281px;
    border-radius: 14px;
    background: var(--card);
    box-shadow: inset 0 0 0 1px var(--card-edge);
  }
  .card--front { left: 137px; }
  .card--back { left: 626px; }

  .photo-frame {
    position: absolute;
    left: 70px;
    top: 75px;
    width: 127px;
    height: 127px;
    border: 4px solid var(--mark-grey);
    border-radius: 8px;
    background: linear-gradient(160deg, #45464a, var(--photo-fill));
  }

  .divider {
    position: absolute; left: 223px; top: 58px;
    width: 1px; height: 165px; background: var(--divider);
  }
  .contact { position: absolute; left: 249px; top: 63px; color: var(--text-white); font-size: 13.5px; line-height: 16px; }
  .contact__name { color: var(--leaf-green); font-size: 19.5px; line-height: 24px; }
  .contact__role { margin-bottom: 11px; }
  .contact__address { margin-bottom: 10px; }
  .contact__list { list-style: none; }
  .contact__list li { display: flex; align-items: center; gap: 7px; height: 16.5px; }
  .contact__icon { width: 10px; height: 10px; fill: var(--leaf-green); flex: none; }

  .brand { position: absolute; left: 64px; top: 104px; display: flex; align-items: center; gap: 18px; color: var(--mark-grey); font-weight: 400; font-size: 50px; }
  .brand__square { width: 72px; height: 72px; border: 4px solid var(--mark-grey); border-radius: 6px; flex: none; }
</style>
</head>
<body>
<main class="canvas">
  <section class="card card--front">
    <div class="photo-frame" role="img" aria-label="Portrait photo of the sales person"></div>
    <div class="divider"></div>
    <div class="contact">
      <p class="contact__name">Daniel Harper</p>
      <p class="contact__role">Managing Director</p>
      <p class="contact__address">12345, Address Goes Here<br>Country Name, 123456.</p>
      <ul class="contact__list">
        <li><svg class="contact__icon" viewBox="0 0 10 10"><path d="M2 0.5l1.6 2-1 1.2c.7 1.5 1.7 2.5 3.2 3.2l1.2-1 2 1.6-1 1.8C4.5 9 1 5.5.3 1.5z"/></svg>044-123 456 789</li>
        <li><svg class="contact__icon" viewBox="0 0 10 10"><path d="M0.5 2h9v6h-9z M0.5 2l4.5 3.5L9.5 2" fill="none" stroke="var(--leaf-green)" stroke-width="1.2"/><path d="M0.5 2h9L5 5.3z"/></svg>info@webname.com</li>
        <li><svg class="contact__icon" viewBox="0 0 10 10"><path d="M4 6L6 4M3.5 5L2 6.5a1.4 1.4 0 0 0 1.5 1.5L5 6.5M6.5 5L8 3.5A1.4 1.4 0 0 0 6.5 2L5 3.5" fill="none" stroke="var(--leaf-green)" stroke-width="1.3" stroke-linecap="round"/></svg>www.websitename.com</li>
      </ul>
    </div>
  </section>

  <section class="card card--back">
    <div class="brand"><span class="brand__square"></span><span class="brand__name">Fernlake</span></div>
  </section>
</main>
</body>
</html>
```